Rollup Poster Design

I need a design for a Pull-up poster for a marketing event. Something simple using the brand and tag line " Do what you do best and leave the rest to us". In addition it should include url: www.larkhollow.sg website not complete yet.
The business is a co-working space focused on helping new business entrepreneurs. It is called Larkhollow Singapore (previously called Quill Forge Singapore). It is located in Singapore in the central business district with offices, desks, a roof terrace and provides services for company set-up in Singapore. Images can be found on the previous website: www.quillforge.sg.
Attached brand images.
Thanks
Tobin

```html
<!DOCTYPE html>
<html lang="en">
<head>
<meta charset="utf-8">
<title>Larkhollow Rollup Poster</title>
<link rel="stylesheet" href="https://fonts.googleapis.com/css2?family=Open+Sans:wght@400;600;700&display=swap">
<style>
  :root {
    --brand-green: #7fbc00;
    --brand-green-light: #b4dc55;
    --brand-green-glow: #d6eca0;
    --paper: #ffffff;
    --backdrop: #d8d8d8;
  }
  html, body {
    margin: 0;
    padding: 0;
    overflow: hidden;
  }
  .canvas {
    position: relative;
    width: 1200px;
    height: 1000px;
    background: var(--backdrop);
    overflow: hidden;
    font-family: "Open Sans", Arial, sans-serif;
  }
  .rollup {
    position: absolute;
    left: 450px;
    top: 148px;
    width: 299px;
    height: 705px;
    background: var(--paper);
  }
  .rollup__top-band {
    position: absolute;
    left: 0;
    top: 0;
    width: 100%;
    height: 18px;
    background: var(--brand-green);
  }
  .brand {
    position: absolute;
    left: 0;
    top: 32px;
    width: 100%;
    text-align: center;
  }
  .brand__mark {
    display: block;
    width: 38px;
    height: 38px;
    margin: 0 auto;
    border-radius: 50%;
    background: var(--brand-green);
  }
  .brand__name {
    display: block;
    margin-top: 0;
    font-size: 38px;
    font-weight: 700;
    line-height: 48px;
    color: var(--brand-green);
    letter-spacing: -0.5px;
  }
  .tagline {
    position: absolute;
    left: 21px;
    top: 189px;
    width: 275px;
    margin: 0;
    font-size: 33px;
    font-weight: 700;
    line-height: 42px;
    color: var(--brand-green);
    letter-spacing: -0.3px;
  }
  .feature {
    position: absolute;
    left: 0;
    top: 0;
    width: 299px;
    height: 705px;
  }
  .rollup__url {
    position: absolute;
    left: 21px;
    top: 655px;
    width: 258px;
    text-align: center;
    font-size: 22px;
    font-weight: 400;
    color: var(--paper);
  }
</style>
</head>
<body>
<div class="canvas">
  <div class="rollup">
    <div class="rollup__top-band"></div>

    <svg class="feature" viewBox="0 0 299 705">
      <defs>
        <radialGradient id="feature-glow" cx="50%" cy="42%" r="60%">
          <stop offset="0%" stop-color="var(--brand-green-glow)"/>
          <stop offset="45%" stop-color="var(--brand-green-light)"/>
          <stop offset="100%" stop-color="var(--brand-green)"/>
        </radialGradient>
      </defs>
      <rect class="feature__base" x="21" y="550" width="257" height="155" fill="var(--brand-green)"/>
      <circle cx="149" cy="495" r="138" fill="var(--paper)"/>
      <circle class="feature__illustration" cx="149" cy="495" r="129" fill="url(#feature-glow)" role="img" aria-label="Large white line illustration of a glowing light bulb with rays"/>
    </svg>

    <div class="brand">
      <span class="brand__mark"></span>
      <span class="brand__name">Larkhollow</span>
    </div>

    <h1 class="tagline">Do what you do best and leave the rest to us</h1>

    <div class="rollup__url">www.larkhollow.sg</div>
  </div>
</div>
</body>
</html>
```